Redesign Website

I currently have a website www.kelvaromotionrx.com that I would like to have redesigned for esthetics and design limitations with the present platform. I will provide my logo, background logo (attached) , current site, foundation grip PSD.zip (attached) and a questionnaire (attached) from a web design company to provide the input to have an impressive site that pleases the eyes and makes an impact. I would also like the site to be mobile friendly.

IMPORTANT:
- The final PSD must include:
o Homepage Mockup
o Internal Pages Mockup
o Mobile site mockup
o Fonts files used in mockup

Final website will be responsive, using the Foundation Framework. Attached you will find a PSD of the Foundation grid – please use this and include with your final PSD. Here is a link for reference:
http://plimtex.com/article/1053/foundation-s-grid-and-photoshop-what-you-

Target Market(s)

Patients for physical therapy

Industry/Entity Type

It Company

Requirements
Must have
• Pages included in the present site. Photos and design should change.
Nice to have
• Should provide information necessary for patients to schedule an appointment
Should not have
• Should not be difficult to read.

```html
<!DOCTYPE html>
<html lang="en">
<head>
<meta charset="utf-8">
<title>Kelvaro Motion RX – Services</title>
<link href="https://fonts.googleapis.com/css2?family=Roboto+Condensed:wght@400;700&family=Open+Sans:wght@400;600&display=swap" rel="stylesheet">
<style>
:root{
  --red:#d6001c;
  --nav-top:#f06a6a;
  --nav-bottom:#cf3a3a;
  --ink:#2b2b2b;
  --muted:#666;
  --footer-bg:#eef0f3;
  --rule:#d5d8dd;
  --white:#fff;
}
*{margin:0;padding:0;box-sizing:border-box}
html,body{width:909px;height:1200px;overflow:hidden;background:var(--white)}
body{position:relative;font-family:"Open Sans",sans-serif;color:var(--ink)}
.abs{position:absolute}
.brand{left:148px;top:14px;display:flex;align-items:center;gap:8px}
.brand-mark{width:30px;height:30px;border-radius:50%;background:var(--red)}
.brand-name{font-family:"Roboto Condensed",sans-serif;font-weight:700;font-size:24px;color:var(--red);line-height:1}
.brand-sub{font-family:"Roboto Condensed",sans-serif;font-weight:700;font-size:11px;color:var(--red);display:block;margin-top:3px}
.top-info{right:166px;top:23px;text-align:right;font-family:"Roboto Condensed",sans-serif;font-size:10px;color:var(--muted);line-height:20px}
.top-info span{margin:0 5px}
.nav{left:0;top:65px;width:909px;height:28px;background:linear-gradient(var(--nav-top),var(--nav-bottom));box-shadow:0 2px 3px rgba(0,0,0,.25)}
.nav ul{list-style:none;position:absolute;left:165px;top:0;display:flex;gap:11px;line-height:28px}
.nav li{font-family:"Roboto Condensed",sans-serif;font-weight:700;font-size:9.5px;color:var(--white);letter-spacing:.1px}
.page-title{left:182px;top:110px;font-family:"Roboto Condensed",sans-serif;font-size:18px;color:var(--red)}
.call{right:207px;top:110px;font-family:"Roboto Condensed",sans-serif;font-size:14px;color:var(--muted)}
.call b{font-weight:400;font-size:18px;color:var(--red)}
.photo{width:264px;height:132px;background:var(--white);border:1px solid #ddd;box-shadow:0 1px 4px rgba(0,0,0,.35);padding:4px}
.photo div{width:100%;height:100%}
.list{list-style:none;font-family:"Roboto Condensed",sans-serif;font-size:14.5px;color:var(--ink)}
.list li{line-height:22px;padding-left:14px;position:relative}
.list li::before{content:"»";position:absolute;left:0;top:-1px;color:var(--red);font-size:13px}
.footer{left:0;top:949px;width:909px;height:251px;background:var(--footer-bg);border-top:1px solid var(--rule)}
.fcol{position:absolute;top:34px;width:120px;font-size:7.5px;line-height:10px;color:var(--muted)}
.fcol h3{font-weight:400;font-size:10.5px;color:var(--ink);margin-bottom:12px}
.fcol p{margin-bottom:10px}
.btn{display:inline-block;background:var(--red);color:var(--white);font-size:8px;padding:5px 10px;border:1px solid #a00}
.tweet{margin-bottom:10px}
.tweet em{font-style:normal;color:var(--red);display:block}
.thumbs{display:grid;grid-template-columns:repeat(3,34px);gap:12px 6px}
.thumbs span{width:34px;height:34px;background:#f7f8fa;border:1px solid #dde0e4}
.signup{display:flex;margin-top:8px}
.signup span{width:102px;height:22px;background:var(--white);border:1px solid #ccc;font-size:6px;line-height:20px;padding-left:6px;color:#888}
.signup b{width:22px;height:22px;background:var(--red);color:var(--white);font-size:8px;line-height:22px;text-align:center}
.base-rule{left:182px;top:1145px;width:545px;border-top:1px solid var(--rule)}
.copy{left:182px;top:1162px;font-size:7px;color:var(--muted)}
.links{right:185px;top:1160px;font-size:8px;color:var(--muted)}
.links span{margin:0 9px;color:#aaa}
</style>
</head>
<body>
<div class="abs brand"><span class="brand-mark"></span><span><span class="brand-name">Kelvaro</span><span class="brand-sub">MOTION RX PHYSICAL THERAPY</span></span></div>
<div class="abs top-info">FREE Consultation +555.201.4870<br>Apoinment<span>|</span>Register</div>
<nav class="abs nav"><ul><li>HOME</li><li>LOCATION</li><li>HOURS</li><li>OUR STORY</li><li>MISSION STATEMENT</li><li>SERVICES</li><li>INSURANCE</li><li>NEW PATIENTS</li><li>CONTACT US</li><li>TESTIMONIALS</li><li>COMMUNITY</li></ul></nav>
<h1 class="abs page-title">Services</h1>
<div class="abs call">Call Now Free : <b>555.201.4870</b></div>

<div class="abs photo" style="left:185px;top:169px"><div role="img" aria-label="Therapist treating a patient's leg on a treatment table" style="background:linear-gradient(#5a6670,#2e3a8a 70%,#c94aa8)"></div></div>
<ul class="abs list" style="left:193px;top:308px"><li>Sports Medicine rehabilitation</li><li>Orthopedic Injury rehabilitation</li><li>Post fracture rehabilitation</li></ul>
<div class="abs photo" style="left:462px;top:170px"><div role="img" aria-label="Hands supporting a patient's foot and ankle" style="background:linear-gradient(135deg,#1c1c1c,#b97d62 55%,#2a3b8c)"></div></div>
<ul class="abs list" style="left:470px;top:308px"><li>Preoperative rehabilitation</li><li>Postoperative rehabilitation</li><li>Spine rehabilitation</li></ul>

<div class="abs photo" style="left:185px;top:410px"><div role="img" aria-label="Soccer player kicking a ball on a grass field" style="background:linear-gradient(#9a5a48,#6f9a2c 35%,#5c8a24)"></div></div>
<ul class="abs list" style="left:193px;top:549px;width:250px"><li style="line-height:14px;margin-bottom:4px">ACL prehab (lower extremity injury prevention program)</li><li>Balance &amp; Proprioception training</li><li>Neurological rehabilitation</li><li>Hand and Upper extremity rehabilitation</li></ul>
<div class="abs photo" style="left:467px;top:410px"><div role="img" aria-label="Therapist coaching a patient on an exercise bike" style="background:linear-gradient(90deg,#2b2f38,#5b6470 50%,#c7508e)"></div></div>
<ul class="abs list" style="left:470px;top:551px"><li>Gait Analysis</li><li>Running Analysis</li></ul>

<div class="abs photo" style="left:185px;top:668px"><div role="img" aria-label="Worker moving boxes on a hand truck" style="background:linear-gradient(90deg,#c9c7c2,#7b6a55 45%,#b99a6e 70%,#d8d5cf)"></div></div>
<ul class="abs list" style="left:193px;top:812px"><li>Worker's Compensation Injuries</li><li>Work Hardening</li><li>Motor Vehicle Injuries</li></ul>

<footer class="abs footer">
  <div class="fcol" style="left:187px">
    <h3>Text blurb</h3>
    <p>Lorem ipsum dolor sit metonsectetur adipiscing elit. Maecenas aac sagittis est. Duis magna odio, sollicitudin in porta ac, ornare a dui. Nulla auctor ante.</p>
    <p>Sollicitudin in porta ac, ornare a dui. Nulla auctor ante.</p>
    <span class="btn">Read More</span>
  </div>
  <div class="fcol" style="left:323px">
    <h3>Latest Tweets</h3>
    <div class="tweet">@Kelvaro Motion RX Contrary to popular belief, Lorem Ipsum is not simply random text.<em>25 minute ago</em></div>
    <div class="tweet">Kelvaro Motion RX<br>Contrary to popular belief, Lorem Ipsum is not simply random text.<em>25 minute ago</em></div>
  </div>
  <div class="fcol" style="left:459px">
    <h3>Photo Stream</h3>
    <div class="thumbs"><span></span><span></span><span></span><span></span><span></span><span></span></div>
  </div>
  <div class="fcol" style="left:596px;width:140px">
    <h3>Newsletter signup</h3>
    <p>Sign up out newsletter to get latest updates.</p>
    <div class="signup"><span>Email Address</span><b>GO</b></div>
  </div>
</footer>
<div class="abs base-rule"></div>
<div class="abs copy">Kelvaro Motion RX Physical Therapy © 2013 All Right Reserved.</div>
<div class="abs links">Links<span>|</span>Links<span>|</span>Links<span>|</span>Links<span>|</span>Links<span>|</span>Links</div>
</body>
</html>
```